Kitchen and custom cabinetry company looking for business card design

We make: * Custom Kitchens, contemporary and traditional kitchens, Vanities, Libraries, Custom Entry Doors, Custom Wine Cellars and Custom Design Furniture. Phone number 555-318-2746. Address: Westhampton NY. Email: BRAVOK@mailbox.example Portfolio at: BRAVOKcabinetry.example I would like moderns fonts and not heavy lines. double side but maybe will use clear plastic. I attached the logo.

```html
<!DOCTYPE html>
<html lang="en">
<head>
<meta charset="utf-8">
<title>BRAVOK Cabinetry – Business Card Options</title>
<link rel="stylesheet" href="https://fonts.googleapis.com/css2?family=Orbitron:wght@500&family=Quicksand:wght@500;700&display=swap">
<style>
  :root{
    --backdrop:#d8cccc;
    --accent:#ff3a12;
    --white:#ffffff;
    --name-grey:#6d7371;
    --clear-light:#f3d9db;
    --clear-dark:#a58d8f;
  }
  *{box-sizing:border-box;margin:0;padding:0}
  html,body{width:1200px;height:1000px;overflow:hidden}
  body{
    background:var(--backdrop);
    font-family:"Quicksand",sans-serif;
    position:relative;
  }
  .option-label{
    position:absolute;
    font-family:"Orbitron",sans-serif;
    font-weight:500;
    font-size:34px;
    letter-spacing:6px;
    color:var(--accent);
  }
  .option-label--clear{left:560px;top:118px}
  .option-label--color{left:110px;top:508px}

  .card{
    position:absolute;
    width:560px;height:320px;
    border-radius:28px;
    overflow:hidden;
    display:flex;
    box-shadow:0 6px 18px rgba(90,70,70,.18);
  }
  .card--clear{left:560px;top:172px;background:linear-gradient(100deg,var(--clear-light),var(--clear-dark))}
  .card--color{left:110px;top:562px}

  .card__brand{
    width:212px;height:100%;
    position:relative;
  }
  .card--color .card__brand{background:var(--white)}
  .card--clear .card__brand{border-right:2px solid var(--white)}

  .brand-name{
    position:absolute;
    left:50%;top:50%;
    transform:translate(-50%,-50%) rotate(-90deg);
    font-weight:700;
    font-size:54px;
    line-height:1;
    letter-spacing:3px;
    white-space:nowrap;
    color:var(--name-grey);
  }

  .card__contact{
    flex:1;
    position:relative;
    color:var(--white);
  }
  .card--color .card__contact{background:var(--accent)}
  .card__contact svg{position:absolute;inset:0}
  .contact-list{
    position:absolute;
    left:36px;top:86px;
    list-style:none;
    font-weight:500;
    font-size:19px;
    line-height:28px;
  }
  .contact-list__phone{letter-spacing:2px}
</style>
</head>
<body>

  <div class="option-label option-label--clear">CLEAR PLASTIC</div>
  <section class="card card--clear" aria-label="Clear plastic card">
    <div class="card__brand">
      <span class="brand-name">BRAVOK</span>
    </div>
    <div class="card__contact">
      <svg width="348" height="320" viewBox="0 0 348 320" aria-hidden="true">
        <g stroke="#fff" stroke-width="2">
          <line x1="0" y1="72" x2="348" y2="72"/>
          <line x1="0" y1="182" x2="348" y2="182"/>
        </g>
        <g fill="#fff">
          <rect x="128" y="32" width="90" height="7"/>
          <rect x="128" y="266" width="90" height="7"/>
        </g>
      </svg>
      <ul class="contact-list">
        <li class="contact-list__phone">555 - 318 - 2746</li>
        <li>BRAVOK@mailbox.example</li>
        <li>BRAVOKcabinetry.example</li>
      </ul>
    </div>
  </section>

  <div class="option-label option-label--color">COLOR</div>
  <section class="card card--color" aria-label="Colour card">
    <div class="card__brand">
      <span class="brand-name">BRAVOK</span>
    </div>
    <div class="card__contact">
      <svg width="348" height="320" viewBox="0 0 348 320" aria-hidden="true">
        <g stroke="#fff" stroke-width="2">
          <line x1="0" y1="72" x2="348" y2="72"/>
          <line x1="0" y1="182" x2="348" y2="182"/>
        </g>
        <g fill="#fff">
          <rect x="128" y="32" width="90" height="7"/>
          <rect x="128" y="266" width="90" height="7"/>
        </g>
      </svg>
      <ul class="contact-list">
        <li class="contact-list__phone">555 - 318 - 2746</li>
        <li>BRAVOK@mailbox.example</li>
        <li>BRAVOKcabinetry.example</li>
      </ul>
    </div>
  </section>

</body>
</html>
```